Ember Crest Business cards

We need business cards for our aviation company called Ember Crest Aviation. The colour scheme is the same as the one in the logo you design (metallic green/ similar to the colours on the aircraft). The design needs to be unique and stand out.

Industry/Entity Type

Business

```html
<!DOCTYPE html>
<html lang="en">
<head>
<meta charset="UTF-8">
<title>Ember Crest Aviation – Business Card</title>
<link rel="stylesheet" href="https://fonts.googleapis.com/css2?family=Quicksand:wght@300;400&display=swap">
<style>
  :root {
    --page: #ffffff;
    --card: #e5e5e5;
    --green: #55b045;
    --ink: #333333;
    --ring-fill: #ffffff;
  }
  * { margin: 0; padding: 0; box-sizing: border-box; }
  html, body {
    width: 1200px;
    height: 976px;
    overflow: hidden;
    background: var(--page);
  }
  .canvas {
    position: relative;
    width: 1200px;
    height: 976px;
    font-family: "Quicksand", sans-serif;
    font-weight: 400;
  }
  .brand-mark {
    position: absolute;
    left: 0;
    top: 137px;
    width: 325px;
    height: 265px;
    display: flex;
    align-items: center;
    justify-content: center;
    color: var(--green);
    font-size: 38px;
    font-weight: 400;
    letter-spacing: 3px;
    line-height: 1.1;
    text-align: center;
    text-transform: uppercase;
  }
  .card {
    position: absolute;
    left: 373px;
    width: 820px;
    height: 469px;
    background: var(--card);
  }
  .card--front { top: 21px; }
  .card--back { top: 504px; height: 466px; }
  .ring {
    position: absolute;
    left: 41px;
    width: 70px;
    height: 70px;
  }
  .card--front .ring { top: 199px; }
  .card--back .ring { top: 197px; }
  .front-name {
    position: absolute;
    left: 160px;
    right: 30px;
    top: 70px;
    height: 330px;
    display: flex;
    flex-direction: column;
    justify-content: center;
    align-items: center;
    color: var(--green);
    font-size: 140px;
    font-weight: 300;
    letter-spacing: 8px;
    line-height: 1.08;
    text-transform: uppercase;
  }
  .company-name {
    position: absolute;
    right: 25px;
    top: 27px;
    color: var(--green);
    font-size: 55px;
    font-weight: 400;
    letter-spacing: 3px;
    text-transform: uppercase;
    white-space: nowrap;
    line-height: 1;
  }
  .contact {
    position: absolute;
    right: 50px;
    top: 122px;
    list-style: none;
    text-align: right;
    color: var(--ink);
    font-size: 23px;
    font-weight: 400;
    line-height: 51px;
    letter-spacing: 1px;
    white-space: nowrap;
  }
</style>
</head>
<body>
<main class="canvas">
  <div class="brand-mark">Ember Crest</div>

  <section class="card card--front">
    <svg class="ring" viewBox="0 0 70 70" aria-hidden="true">
      <circle cx="35" cy="35" r="30" fill="var(--ring-fill)" stroke="var(--green)" stroke-width="8"/>
    </svg>
    <div class="front-name"><span>Ember</span><span>Crest</span></div>
  </section>

  <section class="card card--back">
    <h1 class="company-name">Ember Crest Aviation</h1>
    <svg class="ring" viewBox="0 0 70 70" aria-hidden="true">
      <circle cx="35" cy="35" r="30" fill="var(--ring-fill)" stroke="var(--green)" stroke-width="8"/>
    </svg>
    <ul class="contact">
      <li>Tel: .......................</li>
      <li>E: .........................@................</li>
      <li>A: .................................</li>
      <li>....................................</li>
      <li>.......................................</li>
    </ul>
  </section>
</main>
</body>
</html>
```